Bref créative
BrightHollow Capital Partners
......putting entrepreneurs and investors together
Professional
Marcus Pellow
418 Weldon Avenue
Suite 340
Kelby, OR 97412
brighthollowcap@mailvista.net
I have selected the black & red color scheme on the logo.
Angel Investors/Angel Funds
Seed/Start-up Investment
Private Equity Funds
Venture Capital Funding
Merchant Funding
Receivable/Purchase Order Funding

```html
<!DOCTYPE html>
<html lang="en">
<head>
<meta charset="utf-8">
<title>BrightHollow Capital Partners — Business Card</title>
<link href="https://fonts.googleapis.com/css2?family=Cinzel:wght@600&family=Crimson+Pro:wght@400;600&display=swap" rel="stylesheet">
<style>
  :root {
    --backdrop: #e9e6e2;
    --card-black: #0d0d0d;
    --card-red: #e0151b;
    --card-red-deep: #b50d12;
    --swoosh-white: #ffffff;
    --text-light: #ffffff;
    --name-red: #e8171d;
  }
  html, body {
    margin: 0;
    padding: 0;
    width: 1200px;
    height: 852px;
    overflow: hidden;
    background: var(--backdrop);
  }
  .canvas {
    position: relative;
    width: 1200px;
    height: 852px;
  }
  .business-card {
    position: absolute;
    left: 75px;
    top: 126px;
    width: 1050px;
    height: 600px;
    border-radius: 34px;
    overflow: hidden;
    box-shadow: 0 14px 36px rgba(0,0,0,0.25);
  }
  .card-art {
    position: absolute;
    inset: 0;
  }
  .brand-name {
    position: absolute;
    left: 60px;
    top: 215px;
    margin: 0;
    font-family: "Cinzel", serif;
    font-weight: 600;
    color: var(--text-light);
    line-height: 1;
  }
  .brand-name .brand-main {
    display: block;
    font-size: 60px;
    letter-spacing: 1px;
  }
  .brand-name .brand-sub {
    display: block;
    margin-top: 10px;
    font-size: 22px;
    letter-spacing: 12.5px;
  }
  .holder-name {
    position: absolute;
    right: 120px;
    top: 40px;
    margin: 0;
    font-family: "Crimson Pro", serif;
    font-weight: 600;
    font-size: 32px;
    color: var(--name-red);
  }
  .contact {
    position: absolute;
    right: 60px;
    top: 300px;
    margin: 0;
    font-family: "Crimson Pro", serif;
    font-style: normal;
    font-size: 24px;
    line-height: 32px;
    color: var(--text-light);
    text-align: right;
  }
  .contact .line { display: block; }
  .contact .gap { height: 20px; }
  .contact .with-icon {
    display: flex;
    justify-content: flex-end;
    align-items: center;
    gap: 12px;
  }
  .contact .icon {
    width: 18px;
    height: 18px;
    fill: var(--text-light);
  }
</style>
</head>
<body>
<main class="canvas">
  <article class="business-card">
    <svg class="card-art" viewBox="0 0 1050 600" preserveAspectRatio="none" aria-hidden="true">
      <defs>
        <linearGradient id="redField" x1="0" y1="1" x2="1" y2="0">
          <stop offset="0" stop-color="var(--card-red-deep)"/>
          <stop offset="0.5" stop-color="var(--card-red)"/>
          <stop offset="1" stop-color="var(--card-red-deep)"/>
        </linearGradient>
      </defs>
      <rect width="1050" height="600" fill="url(#redField)"/>
      <path class="white-swoosh" d="M0,0 H1050 V0 C960,150 760,330 520,410 C330,470 150,480 0,475 Z" fill="var(--swoosh-white)"/>
      <path class="black-field" d="M0,0 H975 C890,150 700,310 490,378 C320,432 150,450 0,445 Z" fill="var(--card-black)"/>
    </svg>

    <h1 class="brand-name">
      <span class="brand-main">BRIGHTHOLLOW</span>
      <span class="brand-sub">CAPITAL PARTNERS</span>
    </h1>

    <p class="holder-name">Marcus Pellow</p>

    <address class="contact">
      <span class="line">418 Weldon Avenue</span>
      <span class="line">Suite 340, Kelby, OR 97412</span>
      <span class="line gap"></span>
      <span class="line with-icon">610-555-0142
        <svg class="icon" viewBox="0 0 24 24"><rect x="6" y="1" width="12" height="22" rx="2"/></svg>
      </span>
      <span class="line with-icon">610-555-0178
        <svg class="icon" viewBox="0 0 24 24"><path d="M6.6 10.8c1.4 2.8 3.8 5.2 6.6 6.6l2.2-2.2c.3-.3.7-.4 1-.2 1.1.4 2.3.6 3.6.6.6 0 1 .4 1 1V20c0 .6-.4 1-1 1C10.6 21 3 13.4 3 4c0-.6.4-1 1-1h3.5c.6 0 1 .4 1 1 0 1.3.2 2.5.6 3.6.1.3 0 .7-.2 1z"/></svg>
      </span>
      <span class="line with-icon">brighthollowcap@mailvista.net
        <svg class="icon" viewBox="0 0 24 24"><circle cx="12" cy="12" r="11"/><rect x="6" y="8" width="12" height="8" fill="var(--card-red)"/></svg>
      </span>
    </address>
  </article>
</main>
</body>
</html>
```